Elegant One-Page Flyer That Catches People's Eye

For a series of workshops and zoom calls I am marketing with a colleague of mine, we would like to have an elegant, catchy one-page flyer that entices people to contact us. I am envisioning a one-page flyer (a card that is somewhat larger than a postcard) with great text, layout and images which magnetically draws people to us and is positive and inspiring. Also, if at all possible, a QR code linking it to our websites. Good colours would be shades of blue and green. I am uploading: the Text, our pictures, logos and contact information.

```html
<!DOCTYPE html>
<html lang="en">
<head>
<meta charset="utf-8">
<title>Rising Above Hidden Career Deal Breakers</title>
<link href="https://fonts.googleapis.com/css2?family=Archivo+Black&family=Roboto+Condensed:wght@400;700&family=Roboto:wght@300;400&display=swap" rel="stylesheet">
<style>
  :root {
    --ink: #0b0b0b;
    --paper: #ffffff;
    --sky-top: #3f74b8;
    --sky-mid: #9fbfe0;
    --sky-light: #e6eef7;
    --rock: #4e5864;
    --rock-dark: #232a33;
    --mist: #9aa9b8;
    --rule: #333333;
  }
  * { margin: 0; padding: 0; box-sizing: border-box; }
  html, body { width: 927px; height: 1200px; overflow: hidden; background: var(--paper); }
  .flyer {
    position: relative;
    width: 927px;
    height: 1200px;
    background: var(--paper);
    color: var(--ink);
    font-family: "Roboto", Arial, sans-serif;
  }
  .hero-photo {
    position: absolute;
    left: 0; top: 0;
    width: 927px; height: 624px;
    background:
      linear-gradient(180deg, rgba(0,0,0,0) 55%, rgba(35,42,51,0.55) 100%),
      radial-gradient(ellipse at 65% 35%, var(--sky-light) 0%, rgba(230,238,247,0) 55%),
      linear-gradient(180deg, var(--sky-top) 0%, var(--sky-mid) 35%, var(--sky-light) 55%, var(--mist) 75%, var(--rock) 90%, var(--rock-dark) 100%);
  }
  .headline {
    font-family: "Roboto Condensed", "Arial Narrow", sans-serif;
    font-weight: 700;
    color: var(--ink);
    line-height: 1;
    text-transform: uppercase;
  }
  .headline .line { position: absolute; left: 389px; white-space: nowrap; }
  .headline .intro { top: 44px; font-size: 66px; letter-spacing: 0.5px; }
  .headline .career {
    top: 100px;
    font-family: "Archivo Black", "Arial Black", sans-serif;
    font-size: 104px;
    letter-spacing: -3.5px;
    transform: scaleY(0.92);
    transform-origin: left top;
  }
  .headline .going { top: 198px; font-size: 66px; }
  .headline .want { top: 264px; font-size: 66px; letter-spacing: 0.3px; }
  .hook {
    position: absolute;
    left: 391px;
    top: 341px;
    font-family: "Roboto Condensed", "Arial Narrow", sans-serif;
    font-weight: 700;
    font-size: 27px;
    line-height: 29px;
    color: var(--ink);
    white-space: nowrap;
  }
  .series-title {
    position: absolute;
    left: 71px;
    top: 562px;
    font-family: "Roboto Condensed", "Arial Narrow", sans-serif;
    font-weight: 700;
    font-size: 39.8px;
    letter-spacing: 0.2px;
    color: var(--paper);
    text-shadow: 0 1px 4px rgba(0,0,0,0.5);
    white-space: nowrap;
  }
  .format-band {
    position: absolute;
    left: 0; top: 625px;
    width: 927px; height: 57px;
    background: var(--ink);
    color: var(--paper);
    font-family: "Roboto Condensed", "Arial Narrow", sans-serif;
    font-size: 21.5px;
    line-height: 57px;
    padding-left: 76px;
    white-space: nowrap;
  }
  .format-band strong { font-weight: 700; }
  .section-label {
    position: absolute;
    left: 76px;
    top: 704px;
    font-family: "Roboto Condensed", "Arial Narrow", sans-serif;
    font-weight: 700;
    font-size: 20px;
  }
  .portrait {
    position: absolute;
    width: 100px; height: 100px;
    border-radius: 50%;
    border: 6px solid var(--ink);
  }
  .portrait--maren { left: 81px; top: 744px; background: radial-gradient(circle at 50% 45%, #c9a48e 0%, #7a4a4a 60%, #3b2630 100%); }
  .portrait--corinne { left: 86px; top: 860px; background: radial-gradient(circle at 50% 45%, #e2ccc0 0%, #f1ece8 60%, #d9d4d0 100%); }
  .bio {
    position: absolute;
    left: 207px;
    width: 600px;
    font-family: "Roboto", Arial, sans-serif;
    font-weight: 300;
    font-size: 16px;
    line-height: 20px;
  }
  .bio .name {
    display: block;
    font-family: "Roboto Condensed", "Arial Narrow", sans-serif;
    font-weight: 700;
    font-size: 16px;
  }
  .bio--maren { top: 755px; }
  .bio--corinne { top: 874px; }
  .topics {
    position: absolute;
    left: 85px;
    top: 985px;
    width: 350px;
  }
  .topics h2, .contact h2 {
    font-family: "Roboto Condensed", "Arial Narrow", sans-serif;
    font-weight: 700;
    font-size: 16.5px;
    line-height: 20px;
  }
  .topics ol {
    list-style: none;
    margin-top: 20px;
    font-weight: 300;
    font-size: 16.5px;
    line-height: 20px;
    white-space: nowrap;
  }
  .divider {
    position: absolute;
    left: 498px;
    top: 993px;
    width: 1px;
    height: 133px;
    background: var(--rule);
  }
  .contact { position: absolute; left: 523px; top: 985px; width: 380px; }
  .brand {
    position: absolute;
    top: 1040px;
    font-family: "Roboto Condensed", "Arial Narrow", sans-serif;
    font-weight: 400;
    font-size: 19px;
    color: var(--ink);
    white-space: nowrap;
  }
  .brand--vallat { left: 525px; }
  .brand--truenorth { left: 740px; }
  .contact-card {
    position: absolute;
    font-family: "Roboto Condensed", "Arial Narrow", sans-serif;
    font-size: 16.5px;
    line-height: 20px;
  }
  .contact-card .phone { font-weight: 700; }
  .contact-card--corinne { left: 527px; top: 1073px; }
  .contact-card--maren { left: 784px; top: 1076px; }
  .footer-band {
    position: absolute;
    left: 0; top: 1150px;
    width: 927px; height: 50px;
    background: var(--ink);
  }
</style>
</head>
<body>
<main class="flyer">
  <div class="hero-photo" role="img" aria-label="Photo of a rock climber in a red jacket swinging on a rope above a sunlit mountain range under a blue cloudy sky"></div>

  <h1 class="headline">
    <span class="line intro">Is your</span>
    <span class="line career">Career</span>
    <span class="line going">Going the</span>
    <span class="line want">Way you want?</span>
  </h1>

  <p class="hook">YOU FEEL STUCK? BLOCKED? FRUSTRATED?<br>DON’T KNOW WHAT TO DO ABOUT THIS?</p>

  <p class="series-title">RISING ABOVE HIDDEN CAREER DEAL BREAKERS</p>

  <div class="format-band"><strong>FORMAT:</strong> 4 Mini-Workshops + 2 short Online Group Coaching Sessions between Workshops</div>

  <h2 class="section-label">FACILITATORS:</h2>

  <div class="portrait portrait--maren" role="img" aria-label="Portrait photo of Dr. Maren Holloway"></div>
  <p class="bio bio--maren"><span class="name">Dr. Maren Holloway,</span>PhD, CPC, is an American &amp; Swiss-Trained Work &amp; Organizational Psychologist, ICF-Certified Coach, Board Certified Hypnotherapist, Certified Naturopath (TEN) &amp; Certified Ayurvedic Practitioner.</p>

  <div class="portrait portrait--corinne" role="img" aria-label="Portrait photo of Dr. Corinne Vallat"></div>
  <p class="bio bio--corinne"><span class="name">Dr. Corinne Vallat</span>Ph.D., PCC&nbsp; is a coach and somatic experience practitioner , a team coach with diploma and a certified virtual team coach.</p>

  <section class="topics">
    <h2>Learn to overcome and rise above the 4 top hidden career deal breakers fast:</h2>
    <ol>
      <li>1. Microaggressions</li>
      <li>2.Toxic black box team dynamics</li>
      <li>3. Workplace snakes and other dysfunctional types</li>
      <li>4.&nbsp; Disempowering Subconscious Algorithms</li>
    </ol>
  </section>

  <div class="divider"></div>

  <section class="contact">
    <h2>For&nbsp; dates, venue and further information<br>contact Corinne or Maren at:</h2>
  </section>

  <p class="brand brand--vallat">Vallat Coaching</p>
  <p class="brand brand--truenorth">TrueNorth</p>

  <p class="contact-card contact-card--corinne">Corinne –<br>corinne@vallatcoaching.ch,<br><span class="phone">079 412 66 80.</span></p>
  <p class="contact-card contact-card--maren">Maren –<br>maren@truenorth.ch,<br><span class="phone">076 284 5391</span></p>

  <div class="footer-band"></div>
</main>
</body>
</html>
```